Corvimo Business Card

Corvimo is a young and energetic software development consultancy. We spend our time on the road working with clients on their sites an meeting new potential customers and employees!

We need a sharp, vibrant and memorable business card that will inspires those that receive it to look after it as it oozes quality and is a nice thing in its own right.

We like bold colours and distinctive design. So show us what you can do.

In terms of information on the card, it would be good to see:

* Our logo (Obviously :) )
* Employee name
* Email
* Website address
* Mobile number
* Full company name (Corvimo ltd)
* Registered company number
* Registered company address

Industry/Entity Type

Software

Requirements
Nice to have
• We are thinking that having a QR Code on the business card could be a good way of adding active marketing. It would be good to see if you are able to merge the kind of element in to your designs!

Maybe something special could be achieved using a visual QR Code like those produced at http://www.pixoranta.example/ ? You have our media so feel free to have a play.

```html
<!DOCTYPE html>
<html lang="en">
<head>
<meta charset="utf-8">
<title>Corvimo Business Card</title>
<link rel="stylesheet" href="https://fonts.googleapis.com/css2?family=Baloo+2:wght@600;800&display=swap">
<style>
  :root {
    --stage: #ece9e5;
    --card-red: #c3141d;
    --card-red-dark: #8f0c12;
    --steel-light: #8a8d90;
    --steel-mid: #6b6e71;
    --steel-dark: #4f5254;
    --band-light: #c9d0d5;
    --band-mid: #a3acb3;
    --accent-red: #e3212b;
    --white: #ffffff;
  }
  * { box-sizing: border-box; margin: 0; padding: 0; }
  html, body {
    width: 1200px;
    height: 1000px;
    overflow: hidden;
    background: var(--stage);
    font-family: "Baloo 2", sans-serif;
  }
  .canvas {
    position: relative;
    width: 1200px;
    height: 1000px;
  }
  .card {
    position: absolute;
    width: 700px;
    height: 420px;
    border: 9px solid var(--card-red);
    outline: 2px solid var(--card-red-dark);
    background: radial-gradient(ellipse at 55% 40%, var(--steel-light), var(--steel-mid) 55%, var(--steel-dark));
    box-shadow: 0 14px 30px rgba(0,0,0,0.25);
    overflow: hidden;
  }
  .card--front { left: 60px; top: 50px; }
  .card--back { left: 440px; top: 530px; }

  .brand {
    display: flex;
    align-items: center;
    gap: 14px;
    position: absolute;
    color: var(--accent-red);
    font-weight: 800;
    line-height: 1;
    white-space: nowrap;
  }
  .brand__mark {
    background: var(--accent-red);
  }
  .card--front .brand {
    left: 50%;
    top: 36px;
    transform: translateX(-50%);
    font-size: 88px;
  }
  .card--front .brand__mark { width: 44px; height: 44px; }

  .info-band {
    position: absolute;
    left: 0;
    right: 0;
    top: 148px;
    height: 204px;
    background: linear-gradient(100deg, var(--band-mid), var(--band-light) 45%, var(--band-mid));
    border-top: 5px solid var(--accent-red);
    border-bottom: 5px solid var(--accent-red);
    box-shadow: inset 0 4px 0 var(--white), inset 0 -4px 0 var(--white);
  }
  .employee-name {
    position: absolute;
    left: 0;
    right: 0;
    top: 164px;
    text-align: center;
    color: var(--accent-red);
    font-size: 38px;
    font-weight: 800;
    line-height: 1;
  }
  .details {
    position: absolute;
    left: 0;
    right: 0;
    top: 212px;
    list-style: none;
    text-align: center;
    color: var(--accent-red);
    font-size: 19px;
    font-weight: 600;
    line-height: 1.2;
  }
  .details li::before { content: "\2022  "; }
  .tagline {
    position: absolute;
    left: 0;
    right: 0;
    text-align: center;
    font-size: 14px;
    font-weight: 800;
    letter-spacing: 1.5px;
    text-transform: uppercase;
    color: var(--accent-red);
    line-height: 1.2;
  }
  .card--front .tagline { top: 366px; }

  .card--back .brand {
    left: 50%;
    top: 120px;
    transform: translateX(-50%);
    font-size: 110px;
  }
  .card--back .brand__mark { width: 54px; height: 54px; }
  .card--back .tagline { top: 252px; font-size: 16px; }
  .tagline__mid { color: var(--white); }
</style>
</head>
<body>
<main class="canvas">
  <section class="card card--front" aria-label="Business card front">
    <div class="brand"><span class="brand__mark"></span>Corvimo</div>
    <div class="info-band"></div>
    <h1 class="employee-name">Employee Name</h1>
    <ul class="details">
      <li>Website address</li>
      <li>Mobile number</li>
      <li>Full company name (Corvimo ltd)</li>
      <li>Registered company number</li>
      <li>Registered company address</li>
    </ul>
    <p class="tagline">Software Development Consultancy</p>
  </section>

  <section class="card card--back" aria-label="Business card back">
    <div class="brand"><span class="brand__mark"></span>Corvimo</div>
    <p class="tagline">Software <span class="tagline__mid">Development</span> Consultancy</p>
  </section>
</main>
</body>
</html>
```